Silver Heron Construction Services

Create a business card for my business consulting company
Danielle Vesk, Founder and CEO
4816 Alder Brook Way, Ste 100
Denver, CO. 80451
303.782.4190 cell
dvesk@silverheronconst.example
www.silverheronconst.example

Target Market(s)

Private Equity and Construction Companies

Industry/Entity Type

Business / Sales Consulting

Contact Information for Business Card

Tag Line that says "Where Every Plan Is Built To Stand Strong For Years"

Requirements
Must have
• Logo on both sides of the card.
Nice to have
• Add tagline to the same side of the card as my name and contact info

```html
<!DOCTYPE html>
<html lang="en">
<head>
<meta charset="utf-8">
<title>Silver Heron Construction Services – Business Card</title>
<link href="https://fonts.googleapis.com/css2?family=Montserrat:wght@400;500;600&display=swap" rel="stylesheet">
<style>
  :root {
    --backdrop: #8a8a8c;
    --card: #111111;
    --ink: #ffffff;
    --ink-soft: #e6e6e6;
  }
  * { margin: 0; padding: 0; box-sizing: border-box; }
  html, body { width: 900px; height: 1200px; overflow: hidden; }
  body {
    background: var(--backdrop);
    font-family: "Montserrat", sans-serif;
    color: var(--ink);
    position: relative;
  }
  .card {
    position: absolute;
    left: 133px;
    width: 633px;
    height: 365px;
    background: var(--card);
  }
  .card--front { top: 210px; }
  .card--back { top: 624px; }

  .wordmark {
    position: absolute;
    text-align: center;
    font-weight: 600;
    color: var(--ink);
    text-transform: uppercase;
  }
  .wordmark__name { display: block; line-height: 1.1; }
  .wordmark__sub { display: block; }
  .wordmark__rule { display: block; height: 2px; background: var(--ink); margin-top: 8px; }

  .card--front .wordmark {
    left: 50%;
    top: 158px;
    transform: translateX(-50%);
    width: 310px;
  }
  .card--front .wordmark__name { font-size: 30px; letter-spacing: 0.5px; }
  .card--front .wordmark__sub { font-size: 12px; letter-spacing: 2px; margin-top: 6px; }

  .card--back .wordmark {
    left: 66px;
    top: 164px;
    width: 232px;
  }
  .card--back .wordmark__name { font-size: 22px; letter-spacing: 0.4px; }
  .card--back .wordmark__sub { font-size: 9px; letter-spacing: 1.6px; margin-top: 5px; }

  .divider {
    position: absolute;
    left: 316px;
    top: 96px;
    width: 1px;
    height: 174px;
    background: var(--ink);
  }
  .contact {
    position: absolute;
    left: 335px;
    top: 92px;
  }
  .contact__name {
    font-size: 22px;
    font-weight: 600;
    letter-spacing: 0.6px;
    text-transform: uppercase;
  }
  .contact__role {
    font-size: 14.5px;
    font-weight: 400;
    color: var(--ink-soft);
    margin-top: 4px;
    letter-spacing: 0.4px;
  }
  .contact__address {
    font-size: 14.5px;
    font-style: normal;
    line-height: 25px;
    margin-top: 6px;
    color: var(--ink-soft);
  }
  .contact__list { list-style: none; margin-top: 7px; }
  .contact__item {
    display: flex;
    align-items: center;
    gap: 7px;
    font-size: 14.5px;
    line-height: 24px;
    color: var(--ink-soft);
  }
  .contact__item--phone { letter-spacing: 1.6px; }
  .contact__icon { width: 11px; height: 11px; flex: none; fill: var(--ink); }

  .tagline {
    position: absolute;
    left: 0;
    right: 0;
    top: 313px;
    display: flex;
    align-items: center;
    gap: 7px;
    font-size: 13.5px;
    letter-spacing: 0.9px;
    white-space: nowrap;
  }
  .tagline::before, .tagline::after {
    content: "";
    flex: 1;
    height: 1px;
    background: var(--ink);
  }
</style>
</head>
<body>

  <section class="card card--front">
    <div class="wordmark">
      <span class="wordmark__name">Silver Heron</span>
      <span class="wordmark__sub">Construction Services</span>
      <span class="wordmark__rule"></span>
    </div>
  </section>

  <section class="card card--back">
    <div class="wordmark">
      <span class="wordmark__name">Silver Heron</span>
      <span class="wordmark__sub">Construction Services</span>
      <span class="wordmark__rule"></span>
    </div>

    <div class="divider"></div>

    <div class="contact">
      <h1 class="contact__name">Danielle Vesk</h1>
      <p class="contact__role">Founder and CEO</p>
      <address class="contact__address">
        4816 Alder Brook Way, Ste 100<br>
        Denver, CO. 80451
      </address>
      <ul class="contact__list">
        <li class="contact__item contact__item--phone">
          <svg class="contact__icon" viewBox="0 0 24 24"><path d="M6.6 10.8a15 15 0 0 0 6.6 6.6l2.2-2.2a1 1 0 0 1 1-.25 11.4 11.4 0 0 0 3.6.57 1 1 0 0 1 1 1V20a1 1 0 0 1-1 1A17 17 0 0 1 3 4a1 1 0 0 1 1-1h3.5a1 1 0 0 1 1 1c0 1.25.2 2.45.57 3.6a1 1 0 0 1-.25 1z"/></svg>
          303.782.4190
        </li>
        <li class="contact__item">
          <svg class="contact__icon" viewBox="0 0 24 24"><path d="M2 5h20v14H2z M2 5l10 8 10-8" fill="none" stroke="#fff" stroke-width="2.4"/><path d="M2 5h20l-10 8z"/></svg>
          dvesk@silverheronconst.example
        </li>
        <li class="contact__item">
          <svg class="contact__icon" viewBox="0 0 24 24"><circle cx="12" cy="12" r="9.5" fill="none" stroke="#fff" stroke-width="2"/><path d="M2.5 12h19M12 2.5v19M12 2.5c-5 5-5 14 0 19M12 2.5c5 5 5 14 0 19" fill="none" stroke="#fff" stroke-width="1.6"/></svg>
          www.silverheronconst.example
        </li>
      </ul>
    </div>

    <p class="tagline">Where Every Plan Is Built To Stand Strong For Years</p>
  </section>

</body>
</html>
```